Business Card Design

Its a residential construction company

Industry/Entity Type

Residential

Contact Information for Business Card

Velbrook Homes Pty Ltd,
Dane T Halloway
BSc (Struct), M.Build Sci, Eng. (QPTU), FRC.Aust,
Director, Velbrook Homes Pty Ltd

PO Box 487, Harlow Vale, NSW, 2791. Tel: 048726 5531
email: dane@velbrookhomes.com

```html
<!DOCTYPE html>
<html lang="en">
<head>
<meta charset="utf-8">
<title>Velbrook Homes – Business Card</title>
<link rel="stylesheet" href="https://fonts.googleapis.com/css2?family=Oxygen:wght@400;700&display=swap">
<style>
  :root {
    --backdrop: #e4e2df;
    --card: #ffffff;
    --card-shade: #ececec;
    --brand-blue: #2a3c9c;
    --brand-red: #e02a2c;
    --band-red: #dd2a2c;
    --band-dark: #b81f22;
  }
  * { box-sizing: border-box; margin: 0; padding: 0; }
  html, body {
    width: 1200px;
    height: 818px;
    overflow: hidden;
    background: var(--backdrop);
    font-family: "Oxygen", sans-serif;
  }
  .canvas {
    width: 1200px;
    height: 818px;
    display: flex;
    align-items: center;
    justify-content: center;
  }
  .card {
    position: relative;
    width: 900px;
    height: 520px;
    background: linear-gradient(135deg, var(--card) 0%, var(--card) 55%, var(--card-shade) 100%);
    border-radius: 26px;
    overflow: hidden;
    box-shadow: 0 14px 34px rgba(0,0,0,0.18);
    color: var(--brand-blue);
  }
  .brand {
    position: absolute;
    left: 150px;
    top: 96px;
    display: flex;
    align-items: center;
    gap: 16px;
  }
  .brand__mark {
    width: 44px;
    height: 44px;
    background: var(--brand-blue);
  }
  .brand__name {
    font-size: 42px;
    font-weight: 700;
    text-transform: uppercase;
    letter-spacing: 1px;
    line-height: 1;
    white-space: nowrap;
  }
  .person__name {
    position: absolute;
    left: 270px;
    top: 182px;
    font-size: 36px;
    font-weight: 400;
    line-height: 1.1;
    white-space: nowrap;
  }
  .person__role {
    position: absolute;
    left: 380px;
    top: 236px;
    font-size: 20px;
    color: var(--brand-red);
    line-height: 1;
  }
  .card__guide {
    position: absolute;
    left: 0;
    right: 0;
    top: 264px;
    height: 1.5px;
    background: var(--brand-red);
  }
  .person__credentials {
    position: absolute;
    left: 90px;
    top: 280px;
    font-size: 19px;
    white-space: nowrap;
  }
  .contact {
    position: absolute;
    left: 300px;
    top: 332px;
    font-size: 22px;
    line-height: 1.6;
    list-style: none;
    white-space: nowrap;
  }
  .card__band {
    position: absolute;
    left: 0;
    right: 0;
    bottom: 0;
    height: 62px;
    background: linear-gradient(180deg, var(--band-red) 0%, var(--band-red) 80%, var(--band-dark) 100%);
  }
</style>
</head>
<body>
  <main class="canvas">
    <article class="card">
      <div class="brand">
        <span class="brand__mark"></span>
        <span class="brand__name">Velbrook Homes Pty Ltd</span>
      </div>
      <h1 class="person__name">Dane T Halloway</h1>
      <p class="person__role">Director</p>
      <div class="card__guide"></div>
      <p class="person__credentials">BSc (Struct), M.Build Sci, Eng. (QPTU), FRC.Aust</p>
      <ul class="contact">
        <li class="contact__phone">048726 5531</li>
        <li class="contact__email">dane@velbrookhomes.com</li>
        <li class="contact__address">PO Box 487, Harlow Vale, NSW, 2791</li>
      </ul>
      <div class="card__band"></div>
    </article>
  </main>
</body>
</html>
```